Design a double sided business card

We are looking for a clean, eye-catching, and contemporary design that enhances the brand and presents a premium, professional image. Our preference is for a brown card with black gloss detailing and embossed elements; however, we are open to creative input and design suggestions that best achieve a strong visual impact.

Please see the attached existing business card for reference. We use both black and brown colours consistently across our branding.

On sample provided

```html
<!DOCTYPE html>
<html lang="en">
<head>
<meta charset="utf-8">
<title>Halden – Business Card</title>
<link href="https://fonts.googleapis.com/css2?family=Arimo:wght@400;700&family=Michroma&display=swap" rel="stylesheet">
<style>
  :root {
    --backdrop: #5a5a5a;
    --card-dark: #2e2e2e;
    --card-tan: #c9b59c;
    --accent-tan: #c6b298;
    --emboss-brown: #9c7a58;
    --ink-light: #f4f1ec;
    --rule: #ffffff;
    --divider: #555;
  }
  * { box-sizing: border-box; margin: 0; padding: 0; }
  html, body {
    width: 1200px; height: 1200px; overflow: hidden;
    background: var(--backdrop);
  }
  .canvas { position: relative; width: 1200px; height: 1200px; }

  .card {
    position: absolute; left: 255px; width: 690px; height: 394px; overflow: hidden;
  }
  .card--front { top: 158px; background: var(--card-dark); }
  .card--back { top: 652px; background: var(--card-tan); }

  /* front */
  .front__rule { position: absolute; left: 0; right: 0; top: 371px; height: 3px; background: var(--rule); }
  .front__band { position: absolute; left: 0; right: 0; top: 378px; bottom: 0; background: var(--accent-tan); }
  .front__divider {
    position: absolute; left: 367px; top: 81px; width: 1px; height: 226px;
    background: linear-gradient(to bottom, transparent, var(--divider) 15%, var(--divider) 85%, transparent);
  }
  .brand {
    position: absolute; display: flex; flex-direction: column; align-items: center;
  }
  .brand__square { background: var(--accent-tan); }
  .brand__name {
    font-family: "Michroma", sans-serif; font-weight: 400; letter-spacing: 0.12em;
    color: var(--accent-tan); line-height: 1;
  }
  .front .brand { left: 94px; width: 248px; top: 128px; }
  .front .brand__square { width: 100px; height: 100px; margin-bottom: 22px; }
  .front .brand__name { font-size: 28px; }

  .contact { position: absolute; left: 392px; top: 96px; color: var(--ink-light); font-family: "Arimo", sans-serif; }
  .contact__name {
    font-family: "Michroma", sans-serif; font-size: 21px; color: var(--accent-tan);
    letter-spacing: 0.01em; line-height: 1; margin-bottom: 8px;
  }
  .contact__role { font-size: 15px; margin-bottom: 24px; }
  .contact__address { font-size: 16px; line-height: 21px; margin-bottom: 14px; }
  .contact__list { list-style: none; font-size: 16px; }
  .contact__list li { display: flex; align-items: center; height: 20.5px; }
  .contact__icon { width: 14px; height: 14px; margin-right: 12px; margin-left: 0; flex: none; }

  /* back */
  .card--back .brand { left: 0; right: 0; top: 88px; }
  .card--back .brand__square { width: 156px; height: 156px; margin-bottom: 28px; background: var(--emboss-brown); }
  .card--back .brand__name { font-size: 36px; color: var(--emboss-brown); }
</style>
</head>
<body>
<main class="canvas">
  <section class="card card--front front" aria-label="Business card front">
    <div class="brand">
      <div class="brand__square"></div>
      <span class="brand__name">HALDEN</span>
    </div>
    <div class="front__divider"></div>
    <div class="contact">
      <h1 class="contact__name">ARUN PATEL</h1>
      <p class="contact__role">Director</p>
      <p class="contact__address">The Old Mill Cobbler Lane<br>Eastbridge UB9 4LT</p>
      <ul class="contact__list">
        <li>
          <svg class="contact__icon" viewBox="0 0 16 16"><path d="M3 1l3 3-1.5 2c1 2 3 4 5 5l2-1.5 3 3-2 2C7 14 2 9 1 3z" fill="var(--accent-tan)"/></svg>
          0800 246 7130
        </li>
        <li>
          <svg class="contact__icon" viewBox="0 0 16 16"><rect x="4" y="1" width="8" height="14" rx="1.5" fill="none" stroke="var(--ink-light)" stroke-width="1.4"/></svg>
          07700900412
        </li>
        <li>
          <svg class="contact__icon" viewBox="0 0 16 16"><rect x="1" y="4" width="14" height="9" fill="var(--accent-tan)"/><path d="M1 4l7 5 7-5" fill="none" stroke="var(--card-dark)" stroke-width="1.2"/></svg>
          arun@halden.co.uk
        </li>
        <li>
          <svg class="contact__icon" viewBox="0 0 16 16"><circle cx="8" cy="8" r="7" fill="var(--accent-tan)"/><path d="M8 1v14M1 8h14" stroke="var(--card-dark)" stroke-width="1"/></svg>
          www.halden.co.uk
        </li>
      </ul>
    </div>
    <div class="front__rule"></div>
    <div class="front__band"></div>
  </section>

  <section class="card card--back" aria-label="Business card back">
    <div class="brand">
      <div class="brand__square"></div>
      <span class="brand__name">HALDEN</span>
    </div>
  </section>
</main>
</body>
</html>
```